Lomi Lomi Business
Zielgruppe
Lomi Lomi Massage /Wellnessmassage
Aufgabenstellung
Design, Farbgebung und Maße bitte angelehnt an das Velkaro-Design #22
Format 10,5x21cm Querformat (DIN Lang plus beim Anbieter "Prospektwelle" genannt)
Texte siehe Anhang
Daten bitte in editierbarem Illustrator, oder InDesign-Format

```html
<!DOCTYPE html>
<html lang="de">
<head>
<meta charset="utf-8">
<title>Tobias Wendtland – Hawaiianische Massage &amp; Körperarbeit</title>
<link href="https://fonts.googleapis.com/css2?family=Exo+2:wght@400;500;700;800&display=swap" rel="stylesheet">
<style>
  :root {
    --slate: #575556;
    --cream: #fedba6;
    --leaf: #5b8200;
    --leaf-light: #86b53a;
    --white: #ffffff;
    --skin-dark: #9c6540;
    --skin-mid: #b98660;
    --skin-light: #ded6d0;
  }
  html, body {
    margin: 0;
    padding: 0;
    width: 1200px;
    height: 600px;
    overflow: hidden;
    background: var(--slate);
  }
  .flyer {
    position: relative;
    width: 1200px;
    height: 600px;
    overflow: hidden;
    background: var(--slate);
    font-family: "Exo 2", sans-serif;
  }
  .flyer-shapes {
    position: absolute;
    inset: 0;
  }
  .studio-title {
    position: absolute;
    left: 33px;
    top: 30px;
    margin: 0;
    font-weight: 400;
    font-size: 30px;
    line-height: 40px;
    letter-spacing: 2.4px;
  }
  .studio-title span { display: block; }
  .studio-title .owner { color: var(--white); }
  .studio-title .style { color: var(--cream); }
  .studio-title .field { color: var(--leaf); }
  .offer {
    position: absolute;
    left: 330px;
    top: 245px;
    width: 560px;
    margin: 0;
    text-align: center;
    color: var(--cream);
    font-weight: 700;
    font-size: 24px;
    line-height: 29px;
    letter-spacing: 2.4px;
    transform: rotate(-4.2deg);
    transform-origin: center;
  }
  .prices {
    position: absolute;
    left: 35px;
    top: 430px;
    color: var(--white);
    font-size: 16.5px;
    letter-spacing: 1.6px;
  }
  .prices-heading {
    margin: 0 0 24px;
    color: var(--leaf);
    font-weight: 700;
    font-size: 15px;
  }
  .price-item {
    margin: 0 0 20px;
    line-height: 21px;
  }
  .price-item .service { color: var(--cream); }
</style>
</head>
<body>
<div class="flyer">
  <svg class="flyer-shapes" width="1200" height="600" viewBox="0 0 1200 600" aria-hidden="false">
    <defs>
      <linearGradient id="photoTone" x1="0" y1="0" x2="1" y2="1">
        <stop offset="0" stop-color="var(--skin-light)"/>
        <stop offset="0.3" stop-color="var(--skin-mid)"/>
        <stop offset="0.7" stop-color="var(--skin-dark)"/>
        <stop offset="1" stop-color="#c49a7c"/>
      </linearGradient>
      <path id="badgeArc" d="M125 312 A95 95 0 1 1 315 312 A95 95 0 1 1 125 312"/>
    </defs>

    <path class="wave-cream" fill="var(--cream)"
      d="M503 0 C462 70 458 175 522 255 C592 342 650 425 636 520 C631 560 622 582 612 600 L1200 600 L1200 0 Z"/>
    <path class="wave-leaf" fill="var(--leaf)"
      d="M513 0 C476 70 474 175 540 255 C612 342 672 425 658 520 C653 560 644 582 634 600 L1200 600 L1200 0 Z"/>
    <path class="photo-area" role="img" aria-label="Foto: Entspannte Frau bei einer Rückenmassage, Hand auf dem Rücken"
      fill="url(#photoTone)"
      d="M530 0 C494 70 494 175 560 255 C634 342 692 425 678 520 C673 560 664 582 654 600 L1200 600 L1200 0 Z"/>

    <polygon class="offer-band" fill="var(--leaf)" points="0,296 0,373 925,306 919,229"/>

    <g class="opening-badge">
      <circle cx="220" cy="312" r="127" fill="var(--leaf)"/>
      <circle cx="220" cy="312" r="119" fill="none" stroke="var(--white)" stroke-width="2.5"/>
      <circle cx="220" cy="312" r="90" fill="none" stroke="var(--white)" stroke-width="2.5"/>
      <ellipse class="badge-plant" role="img" aria-label="Illustration: grüner Bambuszweig"
        cx="225" cy="308" rx="55" ry="135" fill="var(--leaf-light)" opacity="0.55"/>
      <text fill="var(--white)" font-family="'Exo 2', sans-serif" font-weight="800" font-size="21" letter-spacing="1">
        <textPath href="#badgeArc" startOffset="5%">PRAXIS</textPath>
      </text>
      <text fill="var(--white)" font-family="'Exo 2', sans-serif" font-weight="800" font-size="21" letter-spacing="1">
        <textPath href="#badgeArc" startOffset="34%">ERÖFFNUNG</textPath>
      </text>
    </g>
  </svg>

  <h1 class="studio-title">
    <span class="owner">Tobias Wendtland</span>
    <span class="style">Hawaiianische</span>
    <span class="field">Massage &amp; Körperarbeit</span>
  </h1>

  <p class="offer">Erhalten Sie Ihre erste Massage<br>zum halben Preis!</p>

  <div class="prices">
    <p class="prices-heading">Preise:</p>
    <p class="price-item"><span class="service">Lomi-Lomi Massage (90 Minuten)</span> 95Euro<br>(Lomi Ganzkörpermassage – Gesamtdauer ca.2 Std.)</p>
    <p class="price-item"><span class="service">Business-Massage (30 Minuten)</span> 35 Euro<br>(z.B. für die Mittagspause – Gesamtdauer ca.45Min)</p>
  </div>
</div>
</body>
</html>
```